Pet sitting and Dog Walking Postcard distributed to new home owners in our target market

We need a two-sided postcard (or rack card, size can be anything rack card size or smaller) that is going in a folder that will be distributed each month to new homeowners in our target area. I would like the design to be similar to our brochure which will be uploaded here for you to see. It needs much less information than the brochure.
Should include services we offer; and our 4 systems: online registration, complimentary consultation, flexible scheduling, visits with reports and photos. Should also include our contact information (website, email, phone). Photos from the brochure can be used. Tagline from the cover of the brochure can be used. Call to action should be: Register on our website today to receive a free consultation and $20 off your first booking (when requesting a service, mention the promo code: welcome20).

```html
<!DOCTYPE html>
<html lang="en">
<head>
<meta charset="utf-8">
<title>Hearthside Pet Care – Postcard</title>
<link rel="stylesheet" href="https://fonts.googleapis.com/css2?family=Oswald:wght@500;600&family=Source+Sans+3:ital,wght@0,400;0,600;0,700;1,400&family=Varela+Round&display=swap">
<style>
  :root{
    --purple:#583f63;
    --purple-dark:#4a3354;
    --green:#4b9f38;
    --green-dark:#3b7f2c;
    --green-bright:#6fd14c;
    --white:#ffffff;
    --ink:#4a3354;
    --rule:#b9b9b9;
    --stage:#b4b4b4;
  }
  *{box-sizing:border-box;margin:0;padding:0}
  html,body{width:1200px;height:903px;overflow:hidden;background:var(--stage)}
  .canvas{position:relative;width:1200px;height:903px}
  .card{position:absolute;width:640px;height:427px;overflow:hidden;box-shadow:0 4px 12px rgba(0,0,0,.25)}
  .card-front{left:40px;top:30px;background:var(--green)}
  .card-back{left:520px;top:470px;background:var(--white)}
  .card-bg{position:absolute;inset:0}
  .abs{position:absolute}

  /* brand name */
  .brand{display:flex;align-items:center;gap:7px;font-family:"Oswald",sans-serif;font-weight:600;letter-spacing:.5px;white-space:nowrap}
  .brand-dot{width:12px;height:12px;border-radius:50%;flex:none}
  .front-brand{left:36px;width:240px;top:98px;justify-content:center;color:var(--white);font-size:21px}
  .front-brand .brand-dot{background:var(--green-bright)}
  .back-brand{left:330px;width:150px;top:62px;justify-content:center;color:var(--purple);font-size:15px}
  .back-brand .brand-dot{background:var(--green);width:9px;height:9px}

  /* front */
  .front-headline{left:36px;width:240px;top:170px;text-align:center;font-family:"Oswald",sans-serif;font-weight:600;color:var(--white);font-size:21px;line-height:28px}
  .front-headline .accent{display:block;color:var(--green-bright)}
  .front-body{left:36px;width:240px;top:236px;text-align:center;font-family:"Varela Round",sans-serif;color:var(--white);font-size:12px;line-height:14.2px}
  .front-url{left:385px;top:352px;width:255px;height:36px;background:var(--purple);border-radius:18px 0 0 18px;display:flex;align-items:center;justify-content:center;font-family:"Varela Round",sans-serif;color:var(--white);font-size:11.5px;letter-spacing:1px}

  /* back: services */
  .services-title{left:32px;width:278px;top:58px;text-align:center;font-family:"Source Sans 3",sans-serif;font-weight:700;font-size:13px;color:var(--white)}
  .accent-green{color:var(--green-bright)}
  .service-list{left:63px;top:80px;list-style:none;font-family:"Source Sans 3",sans-serif;font-weight:600;font-size:8.6px;color:var(--white)}
  .service-row{display:flex;gap:16px;height:16.3px;align-items:center}
  .service{display:flex;align-items:center;gap:5px}
  .tick{width:7px;height:7px;flex:none}

  .intro-title{left:45px;top:140px;font-family:"Source Sans 3",sans-serif;font-weight:700;font-size:13.5px;color:var(--white)}
  .intro-text{left:45px;width:253px;top:162px;font-family:"Source Sans 3",sans-serif;font-size:7.6px;line-height:10px;color:var(--white);text-align:justify}

  .steps{left:48px;top:196px;width:252px;list-style:none}
  .step{position:relative;padding-left:24px;margin-bottom:6px}
  .step-icon{position:absolute;left:0;top:5px;width:18px;height:18px;border-radius:50%;background:var(--white);display:flex;align-items:center;justify-content:center}
  .step-title{font-family:"Source Sans 3",sans-serif;font-weight:700;font-size:8.4px;color:var(--green-bright);line-height:11px}
  .step-text{font-family:"Source Sans 3",sans-serif;font-style:italic;font-size:7px;line-height:9.4px;color:var(--white);text-align:justify}

  .cta{left:31px;top:365px;width:266px;height:43px;background:var(--green);border-radius:0 22px 22px 0;color:var(--white);font-family:"Oswald",sans-serif;font-weight:500}
  .cta-lead{position:absolute;left:17px;top:5px;font-size:7.6px;line-height:11px;letter-spacing:.1px}
  .cta-offer{position:absolute;left:130px;top:7px;height:17px;display:flex;border:1px solid var(--white);border-radius:9px;overflow:hidden;font-size:9px}
  .cta-offer .off{padding:0 6px;display:flex;align-items:center}
  .cta-offer .booking{padding:0 7px;background:var(--white);color:var(--purple);display:flex;align-items:center}
  .cta-note{position:absolute;left:17px;top:29px;font-family:"Source Sans 3",sans-serif;font-style:italic;font-weight:400;font-size:7.4px}

  /* back: mailing side */
  .stamp{left:560px;top:21px;width:62px;height:67px;border:1.5px solid #cfcfcf}
  .address-line{left:358px;width:264px;height:1px;background:var(--rule)}
  .contact-title{left:364px;top:315px;font-family:"Source Sans 3",sans-serif;font-weight:700;font-size:11.5px;letter-spacing:.8px;color:var(--green)}
  .contact-band{left:364px;top:336px;width:210px;height:70px;background:var(--purple)}
  .contact-list{left:356px;top:340px;list-style:none;font-family:"Source Sans 3",sans-serif;font-size:9px;color:var(--white)}
  .contact-item{display:flex;align-items:center;gap:7px;height:22px}
  .contact-icon{width:14px;height:14px;border-radius:50%;background:var(--green);display:flex;align-items:center;justify-content:center;flex:none}
  .dog-photo{left:530px;top:306px;width:100px;height:112px;border-radius:40% 40% 10% 10%;background:radial-gradient(ellipse at 55% 45%,#f6efe2 0%,#e9dcc6 45%,rgba(255,255,255,0) 75%)}
</style>
</head>
<body>
<main class="canvas">

  <!-- FRONT -->
  <section class="card card-front" aria-label="Postcard front">
    <svg class="card-bg" width="640" height="427" viewBox="0 0 640 427" aria-hidden="true">
      <defs>
        <linearGradient id="roomGlow" x1="0" y1="0" x2="1" y2="1">
          <stop offset="0" stop-color="#f2ece3"/>
          <stop offset=".45" stop-color="#d9c2a6"/>
          <stop offset=".75" stop-color="#7d8fa6"/>
          <stop offset="1" stop-color="#c9b9a6"/>
        </linearGradient>
      </defs>
      <rect x="0" y="0" width="640" height="427" fill="#4b9f38"/>
      <rect x="24" y="0" width="10" height="288" rx="5" fill="#3b7f2c"/>
    </svg>
    <div class="abs" role="img" aria-label="Photo: smiling woman on a sofa hugging a brown and white spaniel"
         style="left:190px;top:0;width:450px;height:427px;background:linear-gradient(135deg,#f3eee6 0%,#e2cfb6 40%,#8a9ab0 72%,#cdbca8 100%)"></div>
    <svg class="abs" style="left:0;top:0" width="640" height="427" viewBox="0 0 640 427" aria-hidden="true">
      <path d="M36 0 H276 V250 A120 120 0 0 1 156 370 A120 120 0 0 1 36 250 Z" fill="#583f63"/>
    </svg>

    <div class="abs brand front-brand"><span class="brand-dot"></span>Hearthside Pet Care</div>
    <h1 class="abs front-headline">Prioritize Yourself<span class="accent">We'll Focus on Your Pets</span></h1>
    <p class="abs front-body">Fully Insured and Bonded<br>Professional Pet Care Specialists<br>Proudly Serving Maple Ridge and<br>Surrounding Neighborhoods<br>Since 2004</p>
    <div class="abs front-url">www.hearthsidepets.com</div>
  </section>

  <!-- BACK -->
  <section class="card card-back" aria-label="Postcard back">
    <svg class="card-bg" width="640" height="427" viewBox="0 0 640 427" aria-hidden="true">
      <path d="M0 0 H158 Q60 30 32 120 V427 H0 Z" fill="#4b9f38"/>
      <path d="M32 154 A139 139 0 0 1 310 154 V427 H32 Z" fill="#583f63"/>
      <rect x="10" y="140" width="10" height="287" rx="5" fill="#3b7f2c"/>
    </svg>

    <h2 class="abs services-title">Professional <span class="accent-green">Pet Care Services</span></h2>
    <ul class="abs service-list">
      <li class="service-row"><span class="service"><svg class="tick" viewBox="0 0 8 8"><rect x=".5" y=".5" width="7" height="7" fill="none" stroke="#6fd14c"/><path d="M2 4 L3.5 5.5 L6.5 2" fill="none" stroke="#6fd14c" stroke-width="1.2"/></svg>Day Care and Overnight Boarding</span></li>
      <li class="service-row"><span class="service"><svg class="tick" viewBox="0 0 8 8"><rect x=".5" y=".5" width="7" height="7" fill="none" stroke="#6fd14c"/><path d="M2 4 L3.5 5.5 L6.5 2" fill="none" stroke="#6fd14c" stroke-width="1.2"/></svg>Cat Sitting/Small Pet Sitting</span></li>
      <li class="service-row">
        <span class="service"><svg class="tick" viewBox="0 0 8 8"><rect x=".5" y=".5" width="7" height="7" fill="none" stroke="#6fd14c"/><path d="M2 4 L3.5 5.5 L6.5 2" fill="none" stroke="#6fd14c" stroke-width="1.2"/></svg>Dog Walking</span>
        <span class="service"><svg class="tick" viewBox="0 0 8 8"><rect x=".5" y=".5" width="7" height="7" fill="none" stroke="#6fd14c"/><path d="M2 4 L3.5 5.5 L6.5 2" fill="none" stroke="#6fd14c" stroke-width="1.2"/></svg>Pet Sitting</span>
        <span class="service"><svg class="tick" viewBox="0 0 8 8"><rect x=".5" y=".5" width="7" height="7" fill="none" stroke="#6fd14c"/><path d="M2 4 L3.5 5.5 L6.5 2" fill="none" stroke="#6fd14c" stroke-width="1.2"/></svg>Sleepovers</span>
      </li>
    </ul>

    <h2 class="abs intro-title">Ready To Free Up <span class="accent-green">Your Time?</span></h2>
    <p class="abs intro-text">We are here to uncomplicate your life! Our systems and processes allow for seamless scheduling, service and billing. Give us a few minutes of your time and we will deliver it back to you tenfold!</p>

    <ol class="abs steps">
      <li class="step">
        <span class="step-icon"><svg width="10" height="9" viewBox="0 0 10 9"><rect x=".5" y=".5" width="9" height="6" fill="none" stroke="#583f63"/><path d="M3 8.5 H7" stroke="#583f63"/></svg></span>
        <h3 class="step-title">Online Registration</h3>
        <p class="step-text">Click on the register link on our homepage to begin online registration or submit a request form if you would like more information first.</p>
      </li>
      <li class="step">
        <span class="step-icon"><svg width="10" height="9" viewBox="0 0 10 9"><path d="M1 1 H9 V6 H4 L2 8 V6 H1 Z" fill="#4b9f38"/></svg></span>
        <h3 class="step-title">Complimentary Consultation</h3>
        <p class="step-text">Request a consultation through our online portal. We'll reach out to you if you get stuck! Then we'll coordinate a meeting at your convenience.</p>
      </li>
      <li class="step">
        <span class="step-icon"><svg width="10" height="10" viewBox="0 0 10 10"><rect x=".5" y="1.5" width="9" height="8" fill="none" stroke="#583f63"/><path d="M.5 4 H9.5" stroke="#583f63"/></svg></span>
        <h3 class="step-title">Flexible Scheduling</h3>
        <p class="step-text">Once we've met, we will be able to custom schedule your visits to fit your needs. You can always adjust your schedule through our portal app if your needs change.</p>
      </li>
      <li class="step">
        <span class="step-icon"><svg width="10" height="9" viewBox="0 0 10 9"><rect x=".5" y="2" width="9" height="6.5" rx="1" fill="#583f63"/><circle cx="5" cy="5.2" r="1.8" fill="#fff"/><rect x="3" y=".5" width="4" height="2" fill="#583f63"/></svg></span>
        <h3 class="step-title">Visits with Reports and Photos</h3>
        <p class="step-text">Your pets will be cared for by our elite team of Pet Care Specialists. After each visit, you will receive an emailed report with photo.</p>
      </li>
    </ol>

    <div class="abs cta">
      <p class="cta-lead">Register on our website today<br>to receive a free consultation and</p>
      <p class="cta-offer"><span class="off">$20 off</span><span class="booking">Your First Booking</span></p>
      <p class="cta-note">(when requesting a service, mention the promo code: welcome20)</p>
    </div>

    <div class="abs brand back-brand"><span class="brand-dot"></span>Hearthside Pet Care</div>
    <div class="abs stamp" aria-label="Stamp area"></div>
    <div class="abs address-line" style="top:173px"></div>
    <div class="abs address-line" style="top:212px"></div>
    <div class="abs address-line" style="top:249px"></div>

    <h2 class="abs contact-title">CONTACT US</h2>
    <div class="abs contact-band"></div>
    <ul class="abs contact-list">
      <li class="contact-item"><span class="contact-icon"><svg width="8" height="8" viewBox="0 0 8 8"><path d="M1.5 .8 L3 2.5 L2.2 3.4 Q3 5 4.6 5.8 L5.5 5 L7.2 6.5 L6.3 7.4 Q3.5 7.4 .6 1.7 Z" fill="#fff"/></svg></span>555-014-PAWS</li>
      <li class="contact-item"><span class="contact-icon"><svg width="8" height="6" viewBox="0 0 8 6"><rect x=".4" y=".4" width="7.2" height="5.2" fill="none" stroke="#fff" stroke-width=".8"/><path d="M.4 .4 L4 3.3 L7.6 .4" fill="none" stroke="#fff" stroke-width=".8"/></svg></span>hello@hearthsidepets.com</li>
      <li class="contact-item"><span class="contact-icon"><svg width="8" height="8" viewBox="0 0 8 8"><circle cx="4" cy="4" r="3.4" fill="none" stroke="#fff" stroke-width=".8"/><ellipse cx="4" cy="4" rx="1.5" ry="3.4" fill="none" stroke="#fff" stroke-width=".7"/><path d="M.6 4 H7.4" stroke="#fff" stroke-width=".7"/></svg></span>www.hearthsidepets.com</li>
    </ul>
    <div class="abs dog-photo" role="img" aria-label="Photo: cream labrador puppy lying down with a blue collar"></div>
  </section>

</main>
</body>
</html>
```